Präsentationsvorlagen für Verkaufsgespräche
Zielgruppe
Wir verkaufen hochwertigen Kaffee, der traditionel im Trommelröster langsam geröstet wird. Unsere Zielgruppe sind W/ M 30-70.
Aufgabenstellung
Mit dieser Vorlage möchte ich bei den ersten Verkaufsgesprächen unsere Firma gut repräsentieren. Das wird keine lange Präsentation, soll aber einen ansprechenden Einstieg ins Gespräch sein.
Ein paar Fotos habe ich beigefügt. Texte füge ich später ein, wenn jemand was griffbereit hat, nehme ich aber auch das gerne.

```html
<!DOCTYPE html>
<html lang="de">
<head>
<meta charset="utf-8">
<title>Leonero – Präsentationsvorlagen</title>
<link href="https://fonts.googleapis.com/css2?family=Federo&family=Source+Sans+3:wght@400;600&display=swap" rel="stylesheet">
<style>
  :root {
    --stage: #000000;
    --brown: #5b3a20;
    --brown-deep: #4a2e18;
    --cream: #fbf8f4;
    --ink: #5a381f;
    --line: #c9c2bb;
    --white: #ffffff;
  }
  * { box-sizing: border-box; margin: 0; padding: 0; }
  html, body { width: 1200px; height: 560px; overflow: hidden; background: var(--stage); }
  .deck {
    position: relative; width: 1200px; height: 560px;
    display: grid; grid-template-columns: repeat(3, 392px); grid-template-rows: repeat(2, 276px);
    column-gap: 12px; row-gap: 8px;
  }
  .slide { position: relative; overflow: hidden; background: var(--cream); }
  .slide svg.shape { position: absolute; inset: 0; width: 100%; height: 100%; }
  .photo { position: absolute; inset: 0; }
  .brand {
    position: absolute; font-family: "Source Sans 3", sans-serif; font-weight: 600;
    color: var(--white); font-size: 20px; letter-spacing: 0.5px; line-height: 1;
    display: flex; align-items: center; gap: 6px;
  }
  .brand .dot { width: 9px; height: 9px; border-radius: 50%; background: var(--white); }
  .brand.large { font-size: 34px; }
  .brand.large .dot { width: 14px; height: 14px; }
  .copy {
    position: absolute; font-family: "Source Sans 3", sans-serif; font-size: 7.2px;
    line-height: 10.7px; color: var(--ink); white-space: nowrap;
  }
  .right { text-align: right; }
  .left { text-align: left; }
  .title {
    position: absolute; font-family: "Federo", sans-serif; font-weight: 400; color: var(--ink);
    font-size: 17px; line-height: 1; text-transform: uppercase; white-space: nowrap;
  }
</style>
</head>
<body>
<main class="deck">

  <!-- Slide 1: Koffeinschub -->
  <section class="slide">
    <svg class="shape" viewBox="0 0 392 276" preserveAspectRatio="none">
      <rect width="392" height="276" fill="var(--brown)"/>
      <path d="M292 0 C252 60 222 120 226 180 C228 225 240 255 256 276 L392 276 L392 0 Z" fill="var(--cream)"/>
      <path d="M264 0 C232 60 196 128 204 188 C207 206 212 218 220 224 C214 170 240 92 292 0 Z" fill="var(--brown-deep)"/>
      <path d="M258 0 C226 62 190 130 200 192 C203 208 210 218 220 224" fill="none" stroke="var(--line)" stroke-width="0.8"/>
    </svg>
    <div class="brand large" style="left:22px; top:118px;"><span class="dot"></span>Leonero</div>
    <h2 class="title" style="right:11px; top:160px;">Koffeinschub</h2>
    <div class="copy right" style="right:10px; top:185px;">
      <p>Ein traditionelles Produkt wie Kaffee ständig<br>weiter zu entwickeln und den Markterforder-<br>nissen anzupassen – dieser Herausforderung<br>stellen wir uns täglich.</p>
    </div>
  </section>

  <!-- Slide 2: Feinkost -->
  <section class="slide">
    <div class="photo" role="img" aria-label="Hände halten eine Handvoll gerösteter Kaffeebohnen" style="background: radial-gradient(ellipse at 40% 45%, #7a4a2a 0%, #3b2415 45%, #1a100a 100%);"></div>
    <svg class="shape" viewBox="0 0 392 276" preserveAspectRatio="none">
      <path d="M292 0 C252 60 222 120 226 180 C228 225 240 255 256 276 L392 276 L392 0 Z" fill="var(--cream)"/>
      <path d="M264 0 C232 60 196 128 204 188 C207 206 212 218 220 224 C214 170 240 92 292 0 Z" fill="var(--brown)"/>
      <path d="M258 0 C226 62 190 130 200 192 C203 208 210 218 220 224" fill="none" stroke="var(--line)" stroke-width="0.8"/>
    </svg>
    <div class="brand" style="left:12px; top:66px;"><span class="dot"></span>Leonero</div>
    <div class="copy right" style="right:9px; top:7px;">
      <p>Der bewusste Kaffeetrinker<br>und Konsument ist immer<br>auf der Suche nach hervor-<br>ragenden Kaffeequalitäten<br>.</p>
      <p style="margin-top:2px;">Für Bioläden, Feinkost und<br>Delikatessengeschäfte, Ge-<br>nussläden, Coffeeshops &amp;<br>Elektropartner stellen wir ein anspre-<br>chendes Thekendisplay zur Verfügung.<br>Wir versenden regelmäßig an einen<br>großen Adressenverteiler unsere Liste<br>der Bezugsquelle.</p>
    </div>
    <h2 class="title" style="right:10px; top:160px;">Feinkost</h2>
    <div class="copy right" style="right:9px; top:185px;">
      <p>Wir verlinken Ihren Betrieb auf unserer<br>Website. Fordern Sie ein unverbindliches Ange-<br>bot für ein Probepackage an.</p>
    </div>
  </section>

  <!-- Slide 3: Gastro & Hotel -->
  <section class="slide">
    <div class="photo" role="img" aria-label="Geröstete Kaffeebohnen in einer Röstschaufel" style="background: radial-gradient(ellipse at 70% 50%, #6e4426 0%, #2e1a10 50%, #150c07 100%);"></div>
    <svg class="shape" viewBox="0 0 392 276" preserveAspectRatio="none">
      <g transform="translate(392 0) scale(-1 1)">
        <path d="M292 0 C252 60 222 120 226 180 C228 225 240 255 256 276 L392 276 L392 0 Z" fill="var(--cream)"/>
        <path d="M264 0 C232 60 196 128 204 188 C207 206 212 218 220 224 C214 170 240 92 292 0 Z" fill="var(--brown)"/>
        <path d="M258 0 C226 62 190 130 200 192 C203 208 210 218 220 224" fill="none" stroke="var(--line)" stroke-width="0.8"/>
      </g>
    </svg>
    <div class="brand" style="right:8px; top:66px;"><span class="dot"></span>Leonero</div>
    <div class="copy left" style="left:8px; top:9px;">
      <p>Für ein optimales Ergebnis<br>in der Tasse ist das Wissen<br>über alle wichtigen Para-<br>meter unumgänglich.</p>
      <p style="margin-top:9px;">Eine unserer wesentlichen<br>Kompetenzen ist die lau-<br>fende Schulung Ihrer Mitar<br>beiter, ob equipmenttechnisch oder<br>bei den Zubereitungsarten.<br>Wir laden Sie und Ihre Mitarbeiter ein,<br>intensiv in die Welt des Kaffee einzu-<br>tauchen und Ihr Wissen zu vertiefen</p>
    </div>
    <h2 class="title" style="left:7px; top:160px;">Gastro &amp; Hotel</h2>
    <div class="copy left" style="left:8px; top:185px;">
      <p>Unsere Schulungen finden in unserer an die<br>Rösterei angeschlossenen Bar statt, – praxis-<br>nah und individuell – um rasch und effizient<br>ein perfektes Ergebnis in der Tasse zu erzielen.<br>Mit Freude an der Sache und viel Spaß gehen<br>Ihre Mitarbeiter danach motiviert wieder an<br>die Sache heran und bekommen einen<br>besseren Bezug zum Produkt.</p>
    </div>
  </section>

  <!-- Slide 4: Sorten & Blends -->
  <section class="slide">
    <div class="photo" role="img" aria-label="Drei goldene Kaffeeverpackungen mit Etikett" style="background: linear-gradient(90deg, #d9c9a0 0%, #e8dcb8 35%, #d4c196 60%, #ece8e2 100%);"></div>
    <svg class="shape" viewBox="0 0 392 276" preserveAspectRatio="none">
      <path d="M292 0 C252 60 222 120 226 180 C228 225 240 255 256 276 L392 276 L392 0 Z" fill="var(--cream)"/>
      <path d="M264 0 C232 60 196 128 204 188 C207 206 212 218 220 224 C214 170 240 92 292 0 Z" fill="var(--brown)"/>
      <path d="M258 0 C226 62 190 130 200 192 C203 208 210 218 220 224" fill="none" stroke="var(--line)" stroke-width="0.8"/>
    </svg>
    <div class="brand" style="left:10px; top:66px;"><span class="dot"></span>Leonero</div>
    <div class="copy right" style="right:8px; top:8px;">
      <p>Tracibility – Rückverfolg-<br>barkeit – ist unser Ziel.</p>
      <p style="margin-top:16px;">Wir möchten wissen aus<br>welcher Region, welcher<br>Ernte und welcher Planta-<br>ge oder Kooperative unsere<br>eingekauften Kaffees stammen.</p>
      <p style="margin-top:3px;">Ab einer Jahresmenge von 250 kg er-<br>stellen wir mit Ihnen gemeinsam eine<br>eigene, auf Ihren Geschmack abge-<br>stimmte Mischung mit Ihrem Label.</p>
    </div>
    <h2 class="title" style="right:8px; top:160px; font-size:16px;">Sorten &amp; Blends</h2>
    <div class="copy right" style="right:10px; top:185px;">
      <p>Arabica<br>Sie wächst im Hochland, gilt als hochwertige<br>Bohne und hat weniger Koffein.<br>Sie ist als Pflanze empfindlicher und braucht<br>mehr Pflege, das macht sie mild, aromatisch<br>mit einer edlen Säure.<br>Nicht jeder Arabica Kaffee ist auto-<br>matisch ein hoher Qualitätskaffee.</p>
    </div>
  </section>

  <!-- Slide 5: Die Rösterei -->
  <section class="slide">
    <div class="photo" role="img" aria-label="Kaffeebohnen im Kühlsieb eines Trommelrösters" style="background: radial-gradient(ellipse at 65% 55%, #8a5a3a 0%, #5e3a24 50%, #3a2416 100%);"></div>
    <svg class="shape" viewBox="0 0 392 276" preserveAspectRatio="none">
      <g transform="translate(392 0) scale(-1 1)">
        <path d="M292 0 C252 60 222 120 226 180 C228 225 240 255 256 276 L392 276 L392 0 Z" fill="var(--cream)"/>
        <path d="M264 0 C232 60 196 128 204 188 C207 206 212 218 220 224 C214 170 240 92 292 0 Z" fill="var(--brown)"/>
        <path d="M258 0 C226 62 190 130 200 192 C203 208 210 218 220 224" fill="none" stroke="var(--line)" stroke-width="0.8"/>
      </g>
    </svg>
    <div class="brand" style="right:8px; top:66px;"><span class="dot"></span>Leonero</div>
    <div class="copy left" style="left:6px; top:8px;">
      <p>Die Auswahl dieser Rohkaf-<br>fees und das mischen der<br>Blends ist eine wesentliche<br>Grundlage. Alles Wissen um<br>den Einkauf wäre jedoch<br>nichts wert ohne die Erfah-<br>rung und das handwerkli-<br>che Können der Röstkunst.</p>
      <p style="margin-top:4px;">Die Röstung erfolgt im klassischen<br>traditionellen Trommel-Röstverfahren.<br>Es ist nichts Neues mehr, daß dieses<br>Röstverfahren schonend bei niedriger<br>Temperatur erfolgt, die Bohnen kons-</p>
    </div>
    <h2 class="title" style="left:23px; top:160px;">Die Rösterei</h2>
    <div class="copy left" style="left:6px; top:186px;">
      <p>Im Trommelröster verlieren die Bohnen fast ein<br>Fünftel an Gewicht, aber sie gewinnen enorm<br>an Geschmack und die Aromen entfalten sich<br>besser.<br>Je Blend und Sorte die ideale Balance von<br>Säure, Süße und Bitterkeit zu erreichen,<br>das ist die Kunst.</p>
    </div>
  </section>

  <!-- Slide 6: Die Rösterei (Espresso) -->
  <section class="slide">
    <div class="photo" role="img" aria-label="Espresso läuft aus dem Siebträger in zwei weiße Tassen" style="background: linear-gradient(180deg, #3a3330 0%, #6b5b4e 40%, #c9a070 65%, #efe9e2 100%);"></div>
    <svg class="shape" viewBox="0 0 392 276" preserveAspectRatio="none">
      <path d="M292 0 C252 60 222 120 226 180 C228 225 240 255 256 276 L392 276 L392 0 Z" fill="var(--cream)"/>
      <path d="M264 0 C232 60 196 128 204 188 C207 206 212 218 220 224 C214 170 240 92 292 0 Z" fill="var(--brown)"/>
      <path d="M258 0 C226 62 190 130 200 192 C203 208 210 218 220 224" fill="none" stroke="var(--line)" stroke-width="0.8"/>
    </svg>
    <div class="brand" style="left:12px; top:66px;"><span class="dot"></span>Leonero</div>
    <div class="copy right" style="right:8px; top:8px;">
      <p>Die Auswahl dieser Rohkaf-<br>fees und das mischen der<br>Blends ist eine wesentliche<br>Grundlage. Alles Wissen um<br>den Einkauf wäre jedoch<br>nichts wert ohne die Erfah-<br>rung und das handwerkli-<br>che Können der Röstkunst.</p>
      <p style="margin-top:4px;">Die Röstung erfolgt im klassischen<br>traditionellen Trommel-Röstverfahren.<br>Es ist nichts Neues mehr, daß dieses<br>Röstverfahren schonend bei niedriger<br>Temperatur erfolgt, die Bohnen kons-</p>
    </div>
    <h2 class="title" style="right:27px; top:160px;">Die Rösterei</h2>
    <div class="copy right" style="right:8px; top:186px;">
      <p>Im Trommelröster verlieren die Bohnen fast ein<br>Fünftel an Gewicht, aber sie gewinnen enorm<br>an Geschmack und die Aromen entfalten sich<br>besser.<br>Je Blend und Sorte die ideale Balance von<br>Säure, Süße und Bitterkeit zu erreichen,<br>das ist die Kunst.</p>
    </div>
  </section>

</main>
</body>
</html>
```